Personal Training Studio Checkin App (or URL based)

I would like a simple web based app built for our  business. We have a training studio with a simple business model. All our clients buy sessions in packages either 4, 8, or 12 at a time. We want something that a trainer can pull up and Check in a client. This will record the date and time the client was checked in, by what trainer, and what type of session. This system will keep track of the following:
Whenever a Client Checks in so it will ‘tick off’ a session on their package (ie- they have gone from 11 sessions left to 10 sessions left)
Track what sessions a particular trainer does so we can pay them at the end of the week and look at who they trained, what type of session and how many
Look at client activity: Every time they check in, Recharge their package, any activity related to the client, even if it was admin – like deleting a session that was mistakenly recorded.
This will keep a database of clients added and all their activity
The pdf I have included lays out how I think it would work and the features I want
I would like this to run off an tablora that we have at our front check in counter. It can be an app or a URL that use.
***THIS PROJECT IS NOT SO MUCH ABOUT DESIGN BUT ABOUT FUNCTIONALITY OF THE APPLICATION. IT MUST HAVE THE FEATURES I HAVE ASKED FOR THAT WORK TOGETHER. I AM WILLING TO PAY A LITTLE MORE AS A BONUS IF YOU CAN ACCOMPLISH THIS. ALSO IF I FIN THE RIGHT PERSON THAT CAN DO THIS I WILL MAKE IT A GUARNTEED PROJECT.

- Functionality and Track and record all the info we need

```html
<!DOCTYPE html>
<html lang="en">
<head>
<meta charset="utf-8">
<title>The Stride – Studio Check-in App Screens</title>
<link href="https://fonts.googleapis.com/css2?family=Poppins:wght@400;500;600;700;800&display=swap" rel="stylesheet">
<style>
:root{
  --board:#5f5f60;
  --white:#ffffff;
  --ink:#4a4a4d;
  --ink-soft:#6b6b70;
  --muted:#9a9aa0;
  --field:#ececee;
  --orange:#f2501e;
  --orange-soft:#f7835a;
  --dark-btn:#4d4d50;
  --screen-a:#f3f3f5;
  --screen-b:#d2d3d7;
  --smile:#f6c443;
}
*{box-sizing:border-box;margin:0;padding:0}
html,body{width:1200px;height:3464px;overflow:hidden}
body{background:var(--board);font-family:"Poppins",sans-serif;color:var(--ink);position:relative}
.section-title{position:absolute;left:241px;color:var(--white);font-weight:800;font-size:28px;letter-spacing:-.3px;text-transform:uppercase;line-height:1}
.screen{position:absolute;left:241px;width:718px;height:506px;border-radius:10px;overflow:hidden;
  background:radial-gradient(ellipse at 60% 40%,var(--screen-a) 0%,#e4e4e7 45%,var(--screen-b) 100%);
  box-shadow:0 40px 60px -20px rgba(0,0,0,.45)}
.screen::after{content:"";position:absolute;inset:0;border:5px solid var(--white);border-radius:10px;pointer-events:none;z-index:10}
.ring{position:absolute;inset:0;width:718px;height:506px}
.brand{position:absolute;text-align:center;color:var(--ink);line-height:1}
.brand-name{font-weight:700;font-size:34px;letter-spacing:-.5px;display:block}
.brand-tag{font-weight:700;font-size:8px;letter-spacing:3.6px;display:block;margin-top:5px}
.brand.centered{left:0;right:0;top:34px}
.card{position:absolute;background:var(--white);border-radius:12px;box-shadow:0 10px 30px rgba(0,0,0,.08);z-index:2}
.card.accent{border-top:2px solid var(--orange)}
.card-title{position:absolute;left:0;right:0;text-align:center;font-weight:600;font-size:18px;color:var(--ink)}
.label{position:absolute;font-size:7px;font-weight:700;color:var(--ink);text-transform:uppercase}
.field{position:absolute;height:28px;background:var(--field);border-radius:4px;font-size:8px;color:var(--muted);padding:0 15px;display:flex;align-items:center;justify-content:space-between}
.field svg{width:9px;height:9px}
.next-btn{position:absolute;width:65px;height:25px;background:var(--dark-btn);color:var(--white);border-radius:4px;font-size:8px;font-weight:700;display:flex;align-items:center;justify-content:center;z-index:2}
.menu-btn{position:absolute;left:51px;width:225px;height:50px;background:var(--white);border-radius:8px;box-shadow:0 6px 16px rgba(0,0,0,.06)}
.menu-icon{position:absolute;left:15px;top:-16px;width:52px;height:52px;border-radius:10px;background:var(--ink-soft);display:flex;align-items:center;justify-content:center}
.menu-icon.is-active{background:var(--orange)}
.menu-icon svg{width:30px;height:30px}
.menu-label{position:absolute;left:84px;top:0;height:50px;display:flex;align-items:center;font-size:9px;font-weight:700;text-transform:uppercase;color:var(--ink)}
.menu-arrow{position:absolute;right:14px;top:13px;width:24px;height:24px;border-radius:50%;background:#f0f0f2;display:flex;align-items:center;justify-content:center}
.menu-arrow.is-active{background:var(--dark-btn)}
.menu-arrow svg{width:8px;height:8px}
.hero-photo{position:absolute;left:330px;top:54px;width:388px;height:452px;
  background:radial-gradient(ellipse at 45% 55%,rgba(120,120,124,.85) 0%,rgba(150,150,155,.6) 40%,rgba(200,200,205,0) 72%)}
.tile{position:absolute;width:117px;height:109px;border-radius:10px;background:#f4f4f6;border:1px solid #ececee;display:flex;flex-direction:column;align-items:center;justify-content:center;gap:12px;font-size:8px;font-weight:700;color:var(--ink);text-transform:uppercase}
.tile svg{width:44px;height:44px}
.tile.is-selected{background:var(--dark-btn);color:var(--white);border-color:var(--dark-btn);box-shadow:0 10px 18px rgba(0,0,0,.3)}
.thanks{position:absolute;left:229px;top:3262px;display:flex;align-items:center;gap:24px}
.smile-badge{width:98px;height:98px;border-radius:50%;background:radial-gradient(circle at 40% 35%,#ffe27a,var(--smile) 60%,#e39a1f)}
.thanks-text{color:var(--white);font-weight:700;font-size:63px;letter-spacing:-.5px;line-height:1}
</style>
</head>
<body>

<!-- HOME -->
<div class="section-title" style="top:116px">Home</div>
<section class="screen" style="top:161px">
  <svg class="ring" viewBox="0 0 718 506" aria-hidden="true">
    <defs><linearGradient id="ringHome" x1="1" y1="0" x2="0.3" y2="1"><stop offset="0" stop-color="#f2501e"/><stop offset=".6" stop-color="#f2501e"/><stop offset="1" stop-color="#f2501e" stop-opacity=".15"/></linearGradient></defs>
    <circle cx="522" cy="300" r="205" fill="none" stroke="url(#ringHome)" stroke-width="38"/>
  </svg>
  <div class="hero-photo" role="img" aria-label="Photo of two athletes running toward the viewer in grey training tops"></div>
  <div class="brand" style="left:52px;top:28px;text-align:left">
    <span class="brand-name">THE STRIDE</span>
    <span class="brand-tag">PERSONAL TRAINING STUDIO</span>
  </div>
  <div class="menu-btn" style="top:164px">
    <div class="menu-icon is-active"><svg viewBox="0 0 30 30" fill="none" stroke="#fff" stroke-width="1.6"><circle cx="13" cy="10" r="5"/><path d="M4 25c0-5 4-8 9-8"/><circle cx="21" cy="22" r="4.5"/><path d="M19 22l1.5 1.5 3-3"/></svg></div>
    <div class="menu-label">Client Check In</div>
    <div class="menu-arrow is-active"><svg viewBox="0 0 8 8" fill="none" stroke="#fff" stroke-width="1.4"><path d="M3 1.5L5.5 4 3 6.5"/></svg></div>
  </div>
  <div class="menu-btn" style="top:247px">
    <div class="menu-icon"><svg viewBox="0 0 30 30" fill="none" stroke="#fff" stroke-width="1.6"><circle cx="13" cy="10" r="5"/><path d="M4 25c0-5 4-8 9-8"/><circle cx="21" cy="22" r="4.5"/><path d="M21 19.5v5M18.5 22h5"/></svg></div>
    <div class="menu-label">Add New Client</div>
    <div class="menu-arrow"><svg viewBox="0 0 8 8" fill="none" stroke="#777" stroke-width="1.4"><path d="M3 1.5L5.5 4 3 6.5"/></svg></div>
  </div>
  <div class="menu-btn" style="top:331px">
    <div class="menu-icon"><svg viewBox="0 0 30 30" fill="none" stroke="#fff" stroke-width="1.6"><rect x="5" y="6" width="20" height="14" rx="1"/><path d="M12 20v4M18 20v4M9 25h12M9 10h6M9 13h6M9 16h4"/><rect x="17" y="10" width="5" height="6"/></svg></div>
    <div class="menu-label">Admin Panel</div>
    <div class="menu-arrow"><svg viewBox="0 0 8 8" fill="none" stroke="#777" stroke-width="1.4"><path d="M3 1.5L5.5 4 3 6.5"/></svg></div>
  </div>
</section>

<!-- CLIENT CHECK IN -->
<div class="section-title" style="top:729px">Client Check In</div>
<section class="screen" style="top:776px">
  <svg class="ring" viewBox="0 0 718 506" aria-hidden="true">
    <defs><linearGradient id="ringCheck" x1="1" y1="0" x2="0" y2="1"><stop offset="0" stop-color="#f2501e"/><stop offset=".55" stop-color="#f2501e"/><stop offset=".85" stop-color="#f2501e" stop-opacity=".05"/></linearGradient></defs>
    <circle cx="330" cy="410" r="250" fill="none" stroke="url(#ringCheck)" stroke-width="42"/>
  </svg>
  <div class="brand centered"><span class="brand-name">THE STRIDE</span><span class="brand-tag">PERSONAL TRAINING STUDIO</span></div>
  <div class="card accent" style="left:198px;top:129px;width:310px;height:316px">
    <div class="card-title" style="top:30px">CLIENT CHECK IN</div>
    <div class="label" style="left:31px;top:77px">Client Name:</div>
    <div class="field" style="left:31px;top:88px;width:248px">John Doe</div>
    <div class="label" style="left:31px;top:131px">Session Type:</div>
    <div class="field" style="left:31px;top:142px;width:248px">Select<svg viewBox="0 0 9 9" fill="none" stroke="#555" stroke-width="1.2"><path d="M2 3.5l2.5 2.5L7 3.5"/></svg></div>
    <div class="label" style="left:31px;top:185px">Trainer Name:</div>
    <div class="field" style="left:31px;top:196px;width:248px">David<svg viewBox="0 0 9 9" fill="none" stroke="#555" stroke-width="1.2"><path d="M2 3.5l2.5 2.5L7 3.5"/></svg></div>
    <div class="label" style="left:31px;top:239px">Partner Name:</div>
    <div class="field" style="left:31px;top:250px;width:248px">Michell<svg viewBox="0 0 9 9" fill="none" stroke="#555" stroke-width="1.2"><path d="M2 3.5l2.5 2.5L7 3.5"/></svg></div>
  </div>
  <div class="next-btn" style="left:611px;top:455px">NEXT</div>
</section>

<!-- ADD CLIENT PANEL -->
<div class="section-title" style="top:1360px">Add Client Panel</div>
<section class="screen" style="top:1406px">
  <svg class="ring" viewBox="0 0 718 506" aria-hidden="true">
    <defs><linearGradient id="ringAdd" x1="1" y1="0" x2="0" y2="1"><stop offset="0" stop-color="#f2501e"/><stop offset=".55" stop-color="#f2501e"/><stop offset=".85" stop-color="#f2501e" stop-opacity=".05"/></linearGradient></defs>
    <circle cx="300" cy="400" r="265" fill="none" stroke="url(#ringAdd)" stroke-width="44"/>
  </svg>
  <div class="brand centered"><span class="brand-name">THE STRIDE</span><span class="brand-tag">PERSONAL TRAINING STUDIO</span></div>
  <div class="card accent" style="left:102px;top:129px;width:515px;height:287px">
    <div class="card-title" style="top:38px">ADD CLIENT PANEL</div>
    <div class="label" style="left:27px;top:95px">First Name:</div>
    <div class="field" style="left:27px;top:103px;width:109px">John</div>
    <div class="label" style="left:144px;top:95px">Last Name:</div>
    <div class="field" style="left:144px;top:103px;width:109px">Doe</div>
    <div class="label" style="left:261px;top:95px">Email:</div>
    <div class="field" style="left:261px;top:103px;width:109px">info@example.com</div>
    <div class="label" style="left:379px;top:95px">Phone Number:</div>
    <div class="field" style="left:379px;top:103px;width:109px">+08-123-456-789</div>
    <div class="label" style="left:27px;top:150px">Session Type:</div>
    <div class="field" style="left:27px;top:158px;width:226px">Select<svg viewBox="0 0 9 9" fill="none" stroke="#555" stroke-width="1.2"><path d="M2 3.5l2.5 2.5L7 3.5"/></svg></div>
    <div class="label" style="left:261px;top:150px">Starting Package Session Amount:</div>
    <div class="field" style="left:261px;top:158px;width:227px">$320</div>
    <div class="label" style="left:27px;top:205px">Partner First Name:</div>
    <div class="field" style="left:27px;top:213px;width:109px">Smith</div>
    <div class="label" style="left:144px;top:205px">Partner Last Name:</div>
    <div class="field" style="left:144px;top:213px;width:109px">John</div>
    <div class="label" style="left:261px;top:205px">Email:</div>
    <div class="field" style="left:261px;top:213px;width:109px">info@example.com</div>
    <div class="label" style="left:379px;top:205px">Phone Number:</div>
    <div class="field" style="left:379px;top:213px;width:109px">+08-123-456-789</div>
  </div>
  <div class="next-btn" style="left:617px;top:453px">NEXT</div>
</section>

<!-- ADMIN PANEL -->
<div class="section-title" style="top:1996px">Admin Panel</div>
<section class="screen" style="top:2043px">
  <svg class="ring" viewBox="0 0 718 506" aria-hidden="true">
    <defs><linearGradient id="ringAdmin" x1="1" y1="0" x2="0" y2="1"><stop offset="0" stop-color="#f2501e"/><stop offset=".55" stop-color="#f2501e"/><stop offset=".85" stop-color="#f2501e" stop-opacity=".05"/></linearGradient></defs>
    <circle cx="330" cy="400" r="265" fill="none" stroke="url(#ringAdmin)" stroke-width="40"/>
  </svg>
  <div class="brand centered"><span class="brand-name">THE STRIDE</span><span class="brand-tag">PERSONAL TRAINING STUDIO</span></div>
  <div class="card" style="left:126px;top:122px;width:466px;height:338px">
    <div class="card-title" style="top:30px">ADMIN PANEL</div>
    <div class="tile" style="left:38px;top:76px"><svg viewBox="0 0 44 44" fill="none" stroke="#555" stroke-width="1.4"><circle cx="20" cy="15" r="7"/><path d="M8 34c0-7 5-11 12-11"/><path d="M34 26v12M28 32h12" stroke="#f2501e" stroke-width="1.8"/></svg>Add Client</div>
    <div class="tile" style="left:167px;top:76px"><svg viewBox="0 0 44 44" fill="none" stroke="#555" stroke-width="1.4"><rect x="6" y="7" width="32" height="30" rx="2"/><path d="M6 13h32"/><circle cx="17" cy="22" r="4"/><path d="M10 34c0-5 3-7 7-7s7 2 7 7"/><path d="M28 20h7M28 25h7M28 30h7" stroke="#f2501e"/></svg>Client Details</div>
    <div class="tile is-selected" style="left:296px;top:76px"><svg viewBox="0 0 44 44" fill="none" stroke="#fff" stroke-width="1.4"><rect x="5" y="6" width="34" height="24" rx="1"/><path d="M16 30l-5 9M28 30l5 9M22 30v8"/><circle cx="14" cy="14" r="3"/><path d="M9 24c0-4 2-6 5-6s5 2 5 6"/><path d="M24 26v-4M28 26v-7M32 26v-9M23 16l5-4 4 2 4-5"/></svg>Trainer Report</div>
    <div class="tile" style="left:38px;top:199px"><svg viewBox="0 0 44 44" fill="none" stroke="#555" stroke-width="1.4"><rect x="8" y="6" width="24" height="32" rx="2"/><rect x="15" y="4" width="10" height="5" rx="1"/><path d="M12 15h3M18 15h9M12 21h3M18 21h9M12 27h3M18 27h6"/><path d="M26 34h12M28 31v6M36 31v6" stroke="#f2501e" stroke-width="1.8"/></svg>Trainer Panel</div>
    <div class="tile" style="left:167px;top:199px"><svg viewBox="0 0 44 44" fill="none" stroke="#555" stroke-width="1.4"><rect x="10" y="6" width="24" height="32" rx="2"/><rect x="17" y="4" width="10" height="5" rx="1"/><path d="M14 16l2 2 3-3M14 23l2 2 3-3M14 30l2 2 3-3" stroke="#f2501e"/><path d="M22 17h8M22 24h8M22 31h8"/></svg>Session Report</div>
  </div>
</section>

<!-- ADD A SESSION -->
<div class="section-title" style="top:2617px">Admin Panel</div>
<section class="screen" style="top:2663px">
  <svg class="ring" viewBox="0 0 718 506" aria-hidden="true">
    <defs><linearGradient id="ringSession" x1="1" y1="0" x2="0" y2="1"><stop offset="0" stop-color="#f2501e"/><stop offset=".55" stop-color="#f2501e"/><stop offset=".85" stop-color="#f2501e" stop-opacity=".05"/></linearGradient></defs>
    <circle cx="300" cy="400" r="265" fill="none" stroke="url(#ringSession)" stroke-width="44"/>
  </svg>
  <div class="brand centered"><span class="brand-name">THE STRIDE</span><span class="brand-tag">PERSONAL TRAINING STUDIO</span></div>
  <div class="card accent" style="left:102px;top:129px;width:515px;height:284px">
    <div class="card-title" style="top:36px">ADD A SESSION</div>
    <div class="label" style="left:27px;top:93px">Client Name:</div>
    <div class="field" style="left:27px;top:103px;width:226px">Michell</div>
    <div class="label" style="left:262px;top:93px">Trainer Name:</div>
    <div class="field" style="left:262px;top:103px;width:226px">Johny<svg viewBox="0 0 9 9" fill="none" stroke="#555" stroke-width="1.2"><path d="M2 3.5l2.5 2.5L7 3.5"/></svg></div>
    <div class="label" style="left:27px;top:148px">Session Type:</div>
    <div class="field" style="left:27px;top:158px;width:226px">Select<svg viewBox="0 0 9 9" fill="none" stroke="#555" stroke-width="1.2"><path d="M2 3.5l2.5 2.5L7 3.5"/></svg></div>
    <div class="label" style="left:262px;top:148px">Partner Name:</div>
    <div class="field" style="left:262px;top:158px;width:226px">Sara</div>
    <div class="label" style="left:27px;top:203px">Date:</div>
    <div class="field" style="left:27px;top:213px;width:226px">Select<svg viewBox="0 0 9 9" fill="none" stroke="#777" stroke-width="1"><rect x="1" y="1.5" width="7" height="6.5" rx=".5"/><path d="M1 3.5h7"/></svg></div>
    <div class="label" style="left:262px;top:203px">Time:</div>
    <div class="field" style="left:262px;top:213px;width:226px">Select<svg viewBox="0 0 9 9"><circle cx="4.5" cy="4.5" r="4" fill="#444"/><path d="M4.5 2.3v2.4l1.6 1" stroke="#fff" stroke-width=".9" fill="none"/></svg></div>
  </div>
</section>

<!-- CLOSING -->
<div class="thanks">
  <div class="smile-badge" role="img" aria-label="Smiling emoji badge"></div>
  <div class="thanks-text">Thanks for Watching</div>
</div>

</body>
</html>
```